More Modern Look Required! Industry leading Property Management company needs a new website!

We are wanting to make our website more modern, as we find it is too cluttered, seems "old" and we want a new look. (www.brightholtrm.com)

We are wanting something fresh, clean and responsive, something that aligns with today's social media demands, something that allows our potential customers to immediately get a sense of the type of company we are.

Our current website was created on Wordpress and we will be keeping that core platform but wanting a new look and feel to it. The only thing we want to keep on the website is our "FOR RENT" page, although again we are open to having that look completely different as well (our programmers can adapt the functionality later)

Here is a synopsis of our branding statements:

CORE VALUES:
1. Passion
2. Innovation
3. Integrity (doing the right thing, even when it's difficult)
4. Empathy
5. Education

CORE FOCUS:
Our vision is to be the premier company for the delivery of all aspects of property management showing our passion for this industry, by innovating our service using cutting-edge technology, helping and educating investors to create aspirational and sustainable communities, adding value to their real estate assets, and working in partnership with all stakeholders including residents, showing empathy and integrity.

Brand Essence

When our customers experience our product or service, it brings forth an emotion of absolute trust that we have their best interests at heart

Brand Personality

We are a company that is passionate about our customers, our company and our vision to be leaders in the field of property management. We are visionaries that aren't afraid to use cutting edge technologies to improve our products and service.

Position or Value Proposition

To whom are we speaking?
- real estate investors, including first timers that are giving us their first starter home. They are not "big time" investors, and because they are giving us their first home (in contrast to an investor buying a rental property, often sight unseen) they are more emotionally tied to their property and will require a company that inspires trust and confidence.

What is our brand promise?
- we will do our best to serve our clients, both owners and tenants, to give them prompt communication, clear, concise answers to their questions, and look after their property quickly and competently.

Why is our product different than the competition and why should our customers care?
- Our management product is superior because we use a combination of technology and strict procedures to ensure each client's experience is consistent, each and every time.

Industry/Entity Type

Real Estate and Property Management

Number of Pages Required

5+ page

Requirements
Must have
• Must be compatible on Wordpress, our existing web platform. Please see our existing website at www.brightholtrm.com to familiarize yourself with our current site. Must incorporate For Rent section
Nice to have
• Built in reviews, contact us form, awards page including Resident Laurel Prizes (we just won again for Best Property Management Company, 8 years in a row)
Should not have
• Too many pages. Currently we feel there is too much information on each tab, and we can consolidate into about 5 or 6 tabs.

```html
<!DOCTYPE html>
<html lang="en">
<head>
<meta charset="utf-8">
<title>Brightholt Residential Management</title>
<link rel="stylesheet" href="https://fonts.googleapis.com/css2?family=Audiowide&family=Roboto:wght@400;500;700&display=swap">
<style>
:root{
  --bg-dark:#0c1a21;
  --bg-darker:#081419;
  --bg-footer:#0a161c;
  --blue:#1b8fd8;
  --blue-deep:#0c4566;
  --blue-mid:#115a82;
  --white:#ffffff;
  --muted:#a9bac3;
  --card:#f4f7f9;
  --ink:#333d44;
  --star:#f2b01e;
}
*{margin:0;padding:0;box-sizing:border-box}
html,body{width:1200px;height:5141px;overflow:hidden;background:var(--bg-dark)}
body{font-family:"Roboto",Arial,sans-serif;color:var(--white);position:relative}
.abs{position:absolute}
.display{font-family:"Audiowide","Roboto",sans-serif;letter-spacing:2px;text-transform:uppercase}
.btn{position:absolute;display:flex;align-items:center;justify-content:center;font-size:11px;text-transform:uppercase;letter-spacing:.5px;color:var(--white)}
.btn-solid{background:var(--blue)}
.btn-outline{border:1px solid var(--white)}
.photo{position:absolute}

/* header / hero */
.hero{left:0;top:0;width:1200px;height:650px;background:linear-gradient(180deg,#203743 0%,#1b2e37 40%,#2a4650 70%,#1f5a70 100%)}
.nav{left:0;top:40px;width:1200px;height:30px;font-size:11px}
.nav span{position:absolute;top:8px;white-space:nowrap}
.logo{display:flex;align-items:center;gap:8px}
.logo .mark{width:22px;height:22px;background:var(--white)}
.logo .name{font-family:"Roboto",sans-serif;font-weight:700;font-size:18px;letter-spacing:1px;color:var(--white)}
.hero-title{left:0;width:1200px;text-align:center}
.search{left:176px;top:558px;width:846px;height:54px;background:var(--white);border:2px solid var(--white)}
.field{position:absolute;top:7px;height:38px;border:1px solid #9aa5ab;color:#333;font-size:9px;padding:0 8px;display:flex;align-items:center}
.field .caret{position:absolute;right:8px;top:15px;width:0;height:0;border-left:4px solid transparent;border-right:4px solid transparent;border-top:5px solid #222}

/* properties */
.sec-props{left:0;top:650px;width:1200px;height:584px;background:var(--bg-dark)}
.prop-card{position:absolute;top:140px;width:486px;height:320px}
.prop-card .loc{position:absolute;left:24px;bottom:74px;font-size:11px}
.prop-card .ttl{position:absolute;left:24px;bottom:48px;font-size:13px;font-family:"Audiowide",sans-serif;text-transform:uppercase;letter-spacing:1px}
.prop-card .meta{position:absolute;left:24px;bottom:18px;font-size:8px;color:#dfe7eb;display:flex;gap:14px}
.meta i{display:inline-block;width:8px;height:8px;border-radius:50%;background:var(--blue);margin-right:4px;vertical-align:-1px}
.arrow{position:absolute;font-size:18px;color:var(--white)}

/* mission */
.sec-mission{left:0;top:1234px;width:1200px;height:678px;background:var(--bg-darker)}
.label{font-size:10px;color:var(--blue);text-transform:uppercase;letter-spacing:.5px}
.body-txt{font-size:11.5px;line-height:19px;color:#dbe4e8}
.bullets li{list-style:none;font-size:12px;color:var(--blue);margin-bottom:8px;display:flex;align-items:center}
.bullets li::before{content:"";width:9px;height:9px;border-radius:50%;background:var(--white);margin-right:6px}

/* services */
.sec-services-banner{left:0;top:1912px;width:1200px;height:264px;background:linear-gradient(180deg,#3c3b3f 0%,#5a4b48 45%,#2b3136 100%)}
.sec-services{left:0;top:2176px;width:1200px;height:560px;background:var(--bg-dark)}
.svc{position:absolute;top:62px;width:314px}
.svc .photo{left:0;top:0;width:314px;height:346px}
.svc .hex{position:absolute;left:131px;top:312px}
.svc h3{position:absolute;top:362px;font-family:"Audiowide",sans-serif;font-weight:400;font-size:12px;letter-spacing:1.5px;white-space:nowrap;text-transform:uppercase}
.svc p{position:absolute;top:380px;width:300px;font-size:11px;line-height:18px;color:#dfe6ea}
.svc a{position:absolute;top:418px;font-size:11px;color:var(--blue);text-decoration:none}

/* why */
.sec-why{left:0;top:2736px;width:1200px;height:680px;background:var(--bg-darker)}

/* stats */
.sec-stats{left:0;top:3414px;width:1200px;height:318px;background:var(--blue-deep);border-top:6px solid var(--blue)}
.stat{position:absolute;top:134px;width:140px;text-align:center}
.stat .num{font-size:28px;font-weight:500;margin-top:6px}
.stat .lbl{font-size:12px;text-transform:uppercase}

/* reviews */
.sec-reviews{left:0;top:3732px;width:1200px;height:584px;background:var(--bg-dark)}
.review{position:absolute;top:110px;width:316px;height:336px;background:var(--card);color:var(--ink);text-align:center;padding:0 22px}
.review .avatar{margin:18px auto 0;width:66px;height:66px;border-radius:50%;background:#5e6b74}
.review .who{margin-top:8px;font-size:14px}
.review .date{font-size:11px}
.review .stars{color:var(--star);font-size:15px;letter-spacing:1px;line-height:16px}
.review p{margin-top:8px;font-size:11px;line-height:19px}
.nav-arrow{position:absolute;width:36px;height:40px;background:var(--white);color:#333;display:flex;align-items:center;justify-content:center;font-size:20px}

/* contact */
.sec-contact{left:0;top:4316px;width:1200px;height:574px;background:var(--blue-deep);border-top:6px solid var(--blue)}
.input{position:absolute;border:1px solid #d9e3e9;background:var(--white);color:#333;font-size:9px;padding:8px 10px;height:40px}

/* footer */
.footer{left:0;top:4890px;width:1200px;height:251px;background:var(--bg-footer)}
.f-head{font-family:"Audiowide",sans-serif;font-size:10px;letter-spacing:1.5px;text-transform:uppercase}
.f-list{list-style:none;font-size:11px;line-height:18px}
.f-list li{display:flex;align-items:center;gap:8px}
.dot{display:inline-block;width:13px;height:13px;border-radius:50%;background:var(--blue);flex:none}
</style>
</head>
<body>

<!-- HERO -->
<header class="abs hero">
  <div class="photo" style="left:0;top:0;width:1200px;height:650px;background:linear-gradient(180deg,rgba(20,40,52,.6),rgba(10,30,40,.2) 60%,rgba(20,90,115,.5))" role="img" aria-label="Modern villa with a pool at dusk"></div>
  <nav class="abs nav">
    <span style="left:110px">Home</span>
    <span style="left:188px">Services ⌄</span>
    <span style="left:276px">Rentals ⌄</span>
    <span style="left:364px">Faqs</span>
    <span style="left:440px">About Us</span>
    <div class="abs logo" style="left:520px;top:2px"><span class="mark"></span><span class="name">BRIGHTHOLT</span></div>
    <span style="left:700px;display:flex;align-items:center;gap:6px"><i class="dot"></i>Ph: 204 555 0142</span>
    <span style="left:828px;display:flex;align-items:center;gap:6px;top:8px"><i class="dot"></i>Toll Free: 1 800 555 0199</span>
    <div class="btn btn-solid" style="left:980px;top:-10px;width:106px;height:42px">Contact Us</div>
  </nav>
  <div class="abs hero-title display" style="top:252px;font-size:24px">Welcome to</div>
  <div class="abs hero-title display" style="top:290px;font-size:25px">Brightholt Residential Management</div>
  <div class="abs hero-title" style="top:334px;font-size:11px;line-height:20px;color:#e6edf0">
    Brightholt Residential Management has been serving the winnipeg and surrounding areas since 1997.<br>
    We offer world class management services to investors and tenants in the single family and multifamily rental market.
  </div>
  <div class="abs search">
    <div class="field" style="left:6px;width:160px;display:block;padding-top:4px"><div style="font-size:7px;color:#666">Type of Search</div><div>Buy</div><span class="caret"></span></div>
    <div class="field" style="left:176px;width:160px">Location<span class="caret"></span></div>
    <div class="field" style="left:346px;width:160px">Type<span class="caret"></span></div>
    <div class="field" style="left:516px;width:160px;justify-content:space-between"><span>Min Budget</span><span>/</span><span>Max Budget</span></div>
    <div class="btn btn-solid" style="left:694px;top:2px;width:144px;height:46px">Search</div>
  </div>
</header>

<!-- FEATURED PROPERTIES -->
<section class="abs sec-props">
  <div class="abs label" style="left:0;width:1200px;text-align:center;top:66px">Featured</div>
  <h2 class="abs display" style="left:0;width:1200px;text-align:center;top:86px;font-size:19px;font-weight:400">Properties</h2>
  <div class="abs" style="left:972px;top:80px"><div class="label" style="font-size:8px">View</div><div style="font-size:11px;border-bottom:1px solid #fff;padding-bottom:2px">ALL PROPERTIES</div></div>
  <span class="arrow" style="left:98px;top:284px">←</span>
  <span class="arrow" style="left:1076px;top:284px">→</span>
  <article class="prop-card" style="left:112px">
    <div class="photo" style="left:0;top:0;width:486px;height:320px;background:linear-gradient(180deg,#8fb4d0 0%,#cfd9de 45%,#6d7f5a 80%,#3e4a35 100%)" role="img" aria-label="White modern villa with lake view"></div>
    <div class="loc">Arzier-Le Muids - Switzerland</div>
    <div class="ttl">Atypical villa with lake view</div>
    <div class="meta"><span><i></i>5 BedRooms</span><span><i></i>8 Rooms</span></div>
  </article>
  <article class="prop-card" style="left:602px">
    <div class="photo" style="left:0;top:0;width:486px;height:320px;background:linear-gradient(180deg,#3c5a6c 0%,#4e6a72 45%,#2f5060 70%,#1d3440 100%)" role="img" aria-label="Large apartment building with pool at dusk"></div>
    <div class="loc">Clarens - Switzerland</div>
    <div class="ttl">Large, well-located apartment</div>
    <div class="meta"><span><i></i>5 BedRooms</span><span><i></i>8 Rooms</span><span><i></i>106m2</span></div>
  </article>
  <div class="btn btn-outline" style="left:846px;top:478px;width:116px;height:46px">List With Us</div>
  <div class="btn btn-solid" style="left:974px;top:478px;width:114px;height:46px">View All</div>
</section>

<!-- MISSION -->
<section class="abs sec-mission">
  <div class="abs" style="left:0;top:68px;width:622px;height:5px;background:var(--blue)"></div>
  <div class="photo" style="left:0;top:73px;width:622px;height:538px;background:linear-gradient(180deg,#a9c3dc 0%,#dde5ec 40%,#c7c3bd 70%,#5d7d3d 100%)" role="img" aria-label="Two-storey white family house on a lawn"></div>
  <div class="abs label" style="left:692px;top:212px">About Us</div>
  <h2 class="abs display" style="left:692px;top:228px;font-size:24px;font-weight:400">Our Mission</h2>
  <p class="abs body-txt" style="left:692px;top:260px;width:360px">To create great experiences for both tenants and owners, resulting in long relationships based on empathy, good communication and trust.</p>
  <ul class="abs bullets" style="left:692px;top:318px">
    <li>Innovative Model</li><li>Comprehensive Services</li><li>Core Values</li>
  </ul>
  <div class="btn btn-solid" style="left:692px;top:406px;width:116px;height:48px">Explore Now</div>
</section>

<!-- SERVICES BANNER -->
<section class="abs sec-services-banner" role="img" aria-label="City skyline at sunset">
  <h2 class="abs display" style="left:0;width:1200px;text-align:center;top:100px;font-size:24px;font-weight:400">Our Services</h2>
  <p class="abs" style="left:0;width:1200px;text-align:center;top:150px;font-size:11px">Brightholt Residential Management in Winnipeg offers some of the most premium services available for investors and tenants.</p>
</section>

<!-- SERVICES CARDS -->
<section class="abs sec-services">
  <article class="svc" style="left:130px">
    <div class="photo" style="background:linear-gradient(160deg,#7a6652,#b8a790 50%,#2f3a46)" role="img" aria-label="Property manager showing documents to a couple"></div>
    <svg class="hex" width="52" height="58" viewBox="0 0 52 58"><polygon points="26,1 51,15 51,43 26,57 1,43 1,15" fill="#1b8fd8"/><path d="M15 30 L26 20 L37 30 M19 28 V40 H33 V28" stroke="#fff" stroke-width="2" fill="none"/></svg>
    <h3>Property Management</h3>
    <p>Using the latest technology and specially trained staff, we efficiently manage your property.</p>
    <a>Learn More...</a>
  </article>
  <article class="svc" style="left:468px">
    <div class="photo" style="background:linear-gradient(160deg,#a8b4bf,#d8dee2 45%,#b32c2c 80%,#6d1f1f)" role="img" aria-label="Lease agreement being signed"></div>
    <svg class="hex" width="52" height="58" viewBox="0 0 52 58"><polygon points="26,1 51,15 51,43 26,57 1,43 1,15" fill="#1b8fd8"/><rect x="17" y="18" width="18" height="22" stroke="#fff" stroke-width="2" fill="none"/><path d="M21 24h10M21 29h10M21 34h10" stroke="#fff" stroke-width="2"/></svg>
    <h3>Leasing and Renewals</h3>
    <p>We perform a comprehensive rental market evaluation to maximize your investment.</p>
    <a>Learn More...</a>
  </article>
  <article class="svc" style="left:804px">
    <div class="photo" style="background:linear-gradient(160deg,#e3e6e8,#c9c6c1 50%,#6f7f98)" role="img" aria-label="Maintenance worker repairing a ceiling"></div>
    <svg class="hex" width="52" height="58" viewBox="0 0 52 58"><polygon points="26,1 51,15 51,43 26,57 1,43 1,15" fill="#1b8fd8"/><path d="M15 30 L26 20 L37 30 M19 28 V40 H33 V28" stroke="#fff" stroke-width="2" fill="none"/><circle cx="26" cy="33" r="3" fill="#fff"/></svg>
    <h3>Property Maintenance</h3>
    <p>You'll never have to worry about that midnight call or have to scramble to find a plumber.</p>
    <a>Learn More...</a>
  </article>
  <article class="svc" style="left:1142px">
    <div class="photo" style="background:linear-gradient(160deg,#c9cbcd,#8e8f90)" role="img" aria-label="Home renovation in progress"></div>
    <h3>Rehab Services</h3>
    <p>We provide renovation to help you win.</p>
    <a>Learn More...</a>
  </article>
  <div class="nav-arrow" style="left:1076px;top:200px;width:34px">›</div>
</section>

<!-- WHY CHOOSE US -->
<section class="abs sec-why">
  <div class="abs" style="left:508px;top:70px;width:692px;height:5px;background:var(--blue)"></div>
  <div class="photo" style="left:508px;top:75px;width:692px;height:536px;background:linear-gradient(180deg,#7fa6cf 0%,#cfd8df 40%,#9aa09c 70%,#5b7a3e 100%)" role="img" aria-label="Modern apartment blocks with balconies"></div>
  <div class="abs label" style="left:112px;top:192px">Brightholt Residential Management</div>
  <h2 class="abs display" style="left:112px;top:210px;font-size:24px;font-weight:400">Why Choose Us</h2>
  <p class="abs body-txt" style="left:112px;top:248px;width:356px">Brightholt Residential Management has been recognized and voted multiple times as The Best <span style="color:var(--blue)">Winnipeg Property Management</span> Company by Resident Laurel Prizes. We are intently focussed on serving both owners and tenants and are dedicated to a culture of superior customer service.</p>
  <p class="abs body-txt" style="left:112px;top:360px;width:356px">Whether you own one investment property or ten, the partnership process with Brightholt Residential Management is easy, efficient and rewarding.</p>
  <div class="btn btn-solid" style="left:112px;top:440px;width:116px;height:46px">Learn More</div>
</section>

<!-- STATS -->
<section class="abs sec-stats">
  <h2 class="abs display" style="left:0;width:1200px;text-align:center;top:56px;font-size:23px;font-weight:400">Currently Under Management</h2>
  <div class="stat" style="left:244px">
    <svg width="76" height="80" viewBox="0 0 76 80"><polygon points="38,2 73,21 73,59 38,78 3,59 3,21" fill="#1b8fd8"/><path d="M22 42 L38 26 L54 42 M27 38 V56 H49 V38" stroke="#fff" stroke-width="3" fill="none"/></svg>
    <div class="num">447</div><div class="lbl">Properties</div>
  </div>
  <div class="stat" style="left:528px">
    <svg width="76" height="80" viewBox="0 0 76 80"><polygon points="38,2 73,21 73,59 38,78 3,59 3,21" fill="#1b8fd8"/><rect x="24" y="24" width="28" height="32" stroke="#fff" stroke-width="3" fill="none"/><path d="M30 32h6M40 32h6M30 40h6M40 40h6M35 56v-8h6v8" stroke="#fff" stroke-width="2.5" fill="none"/></svg>
    <div class="num">543</div><div class="lbl">Units</div>
  </div>
  <div class="stat" style="left:818px">
    <svg width="76" height="80" viewBox="0 0 76 80"><polygon points="38,2 73,21 73,59 38,78 3,59 3,21" fill="#1b8fd8"/><circle cx="33" cy="30" r="6" stroke="#fff" stroke-width="3" fill="none"/><path d="M22 56 V46 Q33 36 44 46 V56" stroke="#fff" stroke-width="3" fill="none"/><circle cx="50" cy="50" r="6" stroke="#fff" stroke-width="2.5" fill="none"/></svg>
    <div class="num">317</div><div class="lbl">Investors</div>
  </div>
</section>

<!-- REVIEWS -->
<section class="abs sec-reviews">
  <h2 class="abs display" style="left:0;width:1200px;text-align:center;top:60px;font-size:22px;font-weight:400">Our Reviews</h2>
  <div class="nav-arrow" style="left:90px;top:234px">←</div>
  <div class="nav-arrow" style="left:1072px;top:234px">→</div>
  <article class="review" style="left:112px">
    <div class="avatar" role="img" aria-label="Reviewer avatar"></div>
    <div class="who">Dorian Hale</div><div class="date">5/29/2019</div><div class="stars">★★★★★</div>
    <p>"Keystone Builders has had the privilege of working with Brightholt to do repair work on a number of their properties and it has been nothing but smooth sailing! The company is expertly run and very easy to deal with. It has truly been a pleasure and we look forward to continuing our relationship with them"</p>
  </article>
  <article class="review" style="left:440px">
    <div class="avatar" role="img" aria-label="Reviewer avatar"></div>
    <div class="who">MARCUS BELL</div><div class="date">6/20/2019</div><div class="stars">★★★★★</div>
    <p>"I have known Owen for almost a year now and Brightholt Started managing my rental property a few months ago. I wish i had used them for their services since I bought this property but I guess it is never too late. Great company to deal with and great staff. I highly recommend their services to all in need".</p>
  </article>
  <article class="review" style="left:770px">
    <div class="avatar" role="img" aria-label="Reviewer avatar"></div>
    <div class="who">LENORA T</div><div class="date">2/26/2021</div><div class="stars">★★★★★</div>
    <p>"I want to thank Owen Pryce and Brightholt Residential Management for their expertise and advice. They gave me lots of valuable tips when navigating a very difficult situation. They are a wealth of knowledge! Very grateful for the time they spent guiding me".</p>
  </article>
  <div class="btn btn-outline" style="left:846px;top:472px;width:116px;height:46px">Learn More</div>
  <div class="btn btn-solid" style="left:974px;top:472px;width:114px;height:46px">View All</div>
</section>

<!-- CONTACT -->
<section class="abs sec-contact">
  <div class="photo" style="left:0;top:0;width:598px;height:568px;background:linear-gradient(180deg,#d9dde0 0%,#f2f2f0 35%,#7a6a5c 55%,#2f8f9a 80%,#1d6e7a 100%)" role="img" aria-label="White modern villa with turquoise pool"></div>
  <h2 class="abs display" style="left:598px;width:602px;text-align:center;top:108px;font-size:23px;font-weight:400">Contact Us</h2>
  <div class="input" style="left:670px;top:164px;width:216px">First Name :</div>
  <div class="input" style="left:904px;top:164px;width:216px">Last Name :</div>
  <div class="input" style="left:670px;top:220px;width:216px">Phone :</div>
  <div class="input" style="left:904px;top:220px;width:216px">Email :</div>
  <div class="input" style="left:670px;top:276px;width:450px;height:80px">Message :</div>
  <div class="btn btn-solid" style="left:670px;top:378px;width:116px;height:46px">Submit</div>
</section>

<!-- FOOTER -->
<footer class="abs footer">
  <div class="abs logo" style="left:110px;top:40px"><span class="mark"></span><span class="name" style="color:var(--blue)">BRIGHTHOLT</span></div>
  <p class="abs" style="left:110px;top:96px;width:240px;font-size:11px;line-height:19px;color:#dbe3e7">Brightholt Residential Management has been serving the winnipeg and surrounding areas since 1997.We offer world class management services to investors and tenants in the single family and multifamily rental market.</p>
  <div class="abs f-head" style="left:430px;top:44px">Quick Links</div>
  <ul class="abs f-list" style="left:430px;top:64px"><li>Home</li><li>Services</li><li>Rentals</li><li>Faqs</li><li>About Us</li></ul>
  <div class="abs f-head" style="left:660px;top:44px">Contact Us</div>
  <ul class="abs f-list" style="left:660px;top:66px;line-height:28px"><li><i class="dot"></i>Ph: 204 555 0142</li><li><i class="dot"></i>Toll Free: 1 800 555 0199</li><li><i class="dot"></i>info@brightholtrm.com</li></ul>
  <div class="abs f-head" style="left:968px;top:44px">Follow Us</div>
  <ul class="abs f-list" style="left:968px;top:62px;line-height:28px"><li><i class="dot"></i>Pinwheel</li><li><i class="dot"></i>Murmur</li><li><i class="dot"></i>Lenscape</li><li><i class="dot"></i>Streamly</li></ul>
  <div class="abs" style="left:0;top:220px;width:1200px;text-align:center;font-size:10px;color:#dbe3e7">© 2019 Brightholt Residential Management. All right reserved</div>
</footer>

</body>
</html>
```